Education related business need name card design

We need name card design for long term study agent.
Company name is Harbor Lantern.
We support clients to connect to the world.
Clients are Japanese family who has primary and secondary school students.

Company Logo is reflection of the globe and HL (Harbor Lantern).
Since business is related to education, we would like to show reliability and love to see the world map (atlas) in the name card.

Target Market(s)

late 30's to 50's parents of primary and secondary students who are enthusiastic for education. Secondary school management

Industry/Entity Type

Education

Contact Information for Business Card

Company name, Address, Official position, Name, Phone number, Mobile number, email address,

Font styles to use
Serif
Other font styles liked:
• Century Gothic(logo)

Requirements
Must have
• Since businee is related to education, we would like to show reliability and love to see the world map (atlas) in the name card.

```html
<!DOCTYPE html>
<html lang="en">
<head>
<meta charset="utf-8">
<title>Harbor Lantern – Business Card</title>
<link href="https://fonts.googleapis.com/css2?family=Questrial&display=swap" rel="stylesheet">
<style>
  :root {
    --backdrop: #2b2624;
    --card: #f7f7f6;
    --navy: #0b3a8a;
    --brand-blue: #1d6fc4;
    --sky: #2a86d6;
    --ink: #123f8c;
    --map-sea: #cfe2ef;
    --map-land: #e4c98a;
  }
  * { box-sizing: border-box; margin: 0; padding: 0; }
  html, body {
    width: 1200px; height: 768px; overflow: hidden;
    background: var(--backdrop);
    font-family: "Questrial", "Century Gothic", sans-serif;
  }
  .stage {
    width: 1200px; height: 768px;
    display: flex; align-items: center; justify-content: center; gap: 40px;
  }
  .card {
    position: relative;
    width: 540px; height: 310px;
    background: var(--card);
    overflow: hidden;
  }

  /* Front */
  .card--front {
    display: flex; flex-direction: column; align-items: center; justify-content: center; gap: 18px;
  }
  .brand-mark {
    width: 96px; height: 96px; border-radius: 50%;
    background: var(--brand-blue);
  }
  .brand-name {
    color: var(--navy);
    font-size: 30px;
    letter-spacing: 0.2px;
  }

  /* Back */
  .side-band {
    position: absolute; left: 0; top: 0; bottom: 0;
    width: 40px; background: var(--navy);
  }
  .side-band::after {
    content: ""; position: absolute; right: -10px; top: 0; bottom: 0;
    width: 6px; background: var(--sky);
  }
  .card-body { position: absolute; left: 80px; top: 30px; right: 30px; bottom: 20px; }
  .brand-lockup { display: flex; align-items: center; gap: 12px; }
  .brand-lockup .brand-mark { width: 66px; height: 66px; }
  .brand-lockup .brand-name { font-size: 26px; line-height: 1.0; }
  .holder { margin-top: 16px; }
  .holder-name { color: var(--ink); font-size: 21px; }
  .holder-title { color: var(--sky); font-size: 12px; margin-top: 2px; }
  .contacts { list-style: none; margin-top: 16px; color: var(--ink); font-size: 14px; line-height: 1.45; }
  .contacts li { display: flex; align-items: center; gap: 10px; }
  .contacts svg { width: 12px; height: 12px; flex: none; fill: var(--ink); }
  .contacts .address { padding-left: 0; }
  .map-atlas {
    position: absolute; right: 40px; bottom: 26px;
    width: 120px; height: 74px; border-radius: 50%;
    background: radial-gradient(ellipse at 45% 50%, var(--map-land) 0%, #c8d9a6 35%, var(--map-sea) 75%);
  }
</style>
</head>
<body>
<main class="stage">
  <section class="card card--front">
    <div class="brand-mark"></div>
    <p class="brand-name">Harbor Lantern Pte.Ltd.</p>
  </section>

  <section class="card card--back">
    <div class="side-band"></div>
    <div class="card-body">
      <div class="brand-lockup">
        <div class="brand-mark"></div>
        <p class="brand-name">Harbor<br>Lantern Pte.Ltd.</p>
      </div>
      <div class="holder">
        <p class="holder-name">Your Long name</p>
        <p class="holder-title">Your Title</p>
      </div>
      <ul class="contacts">
        <li><svg viewBox="0 0 12 12"><path d="M1 2.5C1 1.6 1.6 1 2.5 1h7C10.4 1 11 1.6 11 2.5V4H8V3H4v1H1zM2 5h8l1 6H1z"/></svg>+00 111 222 3333</li>
        <li><svg viewBox="0 0 12 12"><path d="M1 2h10v8H1z M1.6 2.6 6 6.4l4.4-3.8" stroke="#f7f7f6" stroke-width="0.9"/></svg>yourname@yourwebsite.com</li>
        <li><svg viewBox="0 0 12 12"><circle cx="6" cy="6" r="5"/><path d="M1 6h10M6 1c-2 2.5-2 7.5 0 10M6 1c2 2.5 2 7.5 0 10" stroke="#f7f7f6" stroke-width="0.8" fill="none"/></svg>www.yourwebsite.com</li>
        <li class="address">Your Long Commercial or business address</li>
      </ul>
    </div>
    <div class="map-atlas" role="img" aria-label="Oval world map atlas"></div>
  </section>
</main>
</body>
</html>
```